One page site for a home improvement construction company

Looking for a nice, SEO-friendly, single page site for a local handyman. Here's a good example of a similar site: https://pinecrestbuildersnv.com/

My handyman client has many photos of projects (included), so we'd like a nice photo gallery, along with the usual stuff: google map embed, nice contact form (use Elementor native), maybe a place for a few inspirational quotes.

Important: we don't want to use anything other than Elementor Pro and (maybe) a few free plugins to do your design.

Name of business is “Gareth Woolsey Home Improvement”

Target Market(s)

Homeowners in upscale communities

Coding

Coded - Design and coding required

Number of Pages Required

1 page

Font styles to use
Serif
Sans Serif

Requirements
Must have
• Must be Built in Elementor. Needs a photo gallery (project portfolio) section with supplied photos.
Nice to have
• A place for an inspirational quote
Should not have
• The top photo should not be Gareth, it should be about the work.

```html
<!DOCTYPE html>
<html lang="en">
<head>
<meta charset="utf-8">
<title>Gareth Woolsey Home Improvement</title>
<link href="https://fonts.googleapis.com/css2?family=Lato:wght@300;400;700;900&family=Lora:wght@400&display=swap" rel="stylesheet">
<style>
:root{
  --orange:#f26a1b;
  --navy:#1c3459;
  --blue:#1f5fa8;
  --dark:#232323;
  --ink:#222;
  --muted:#555;
  --white:#fff;
  --footer:#1b1b1b;
}
*{box-sizing:border-box;margin:0;padding:0}
html,body{width:1200px;height:5333px;overflow:hidden}
body{position:relative;font-family:"Lato",sans-serif;color:var(--ink);background:var(--white)}
.abs{position:absolute}
section,header,footer{position:absolute;left:0;width:1200px}

/* header */
.site-header{top:0;height:103px;background:var(--white)}
.brand-mark{left:132px;top:18px;width:76px;height:64px;background:#5a3a22}
.brand-name{left:224px;top:40px;font-weight:900;font-size:21px;letter-spacing:.2px;color:#222;line-height:1}
.brand-sub{left:226px;top:64px;font-size:15px;letter-spacing:3px;color:#222;line-height:1}
.follow{left:703px;top:28px;font-size:11px;color:#333}
.social{width:26px;height:26px;border-radius:50%;top:21px}
.call-label{left:941px;top:18px;font-size:11px;color:#333}
.call-number{left:941px;top:32px;font-size:20px;font-weight:700;color:var(--orange)}
.nav{top:68px;font-size:12.5px;font-weight:700;color:#222;letter-spacing:.3px}
.nav.active{color:var(--orange);text-decoration:underline}

/* hero */
.hero{top:103px;height:629px;background:linear-gradient(160deg,#5d6b3c 0%,#8a5a34 35%,#6a4a32 55%,#3e4a2f 80%,#2c3a5a 100%)}
.hero-eyebrow{left:120px;top:215px;font-size:36px;font-weight:300;color:var(--white);letter-spacing:.5px}
.hero-title{left:120px;top:258px;font-size:44px;font-weight:900;color:var(--white);line-height:54px}
.btn{background:var(--orange);color:var(--white);font-weight:700;text-align:center;text-transform:uppercase}
.hero-btn{left:124px;top:377px;width:178px;height:50px;line-height:50px;font-size:15px}
.hero-arrow{top:280px}

/* welcome */
.welcome{top:732px;height:497px;background:var(--dark)}
.portrait{left:178px;top:77px;width:356px;height:356px;border-radius:50%;border:7px solid var(--blue);background:radial-gradient(circle at 50% 40%,#7c8aa0,#3f5a7c 60%,#2b3f5a)}
.welcome-kicker{left:623px;top:68px;font-size:30px;color:var(--white)}
.welcome-title{left:623px;top:100px;font-size:38px;color:var(--white)}
.rule{height:3px;background:var(--orange)}
.welcome-text{left:623px;top:196px;width:440px;font-size:14px;line-height:22.5px;color:#d8d8d8}
.welcome-btn{left:627px;top:387px;width:120px;height:37px;line-height:37px;font-size:12.5px}

/* services */
.services{top:1229px;height:571px;background:linear-gradient(180deg,#1f3b66 0%,#1b3258 60%,#1c3a66 100%)}
.section-title{width:1200px;left:0;text-align:center;font-weight:700;font-size:38px}
.title-bar{left:576px;width:48px;height:3px}
.service{width:260px;text-align:center;color:var(--white);font-size:14px;font-weight:700;line-height:18px}
.service svg{display:block;margin:0 auto 14px}

/* projects */
.projects{top:1800px;height:1334px;background:var(--white)}
.tile{background:#7a5a3e}
.tile-feature{background:linear-gradient(160deg,#245aa2,#1d4a88);color:var(--white);text-align:center}
.tile-feature h3{font-size:24px;font-weight:700;line-height:28px;margin-top:98px}
.tile-feature .btn{display:inline-block;margin-top:14px;width:186px;height:36px;line-height:36px;font-size:12.5px}

/* testimonials */
.testimonials{top:3134px;height:621px;background:linear-gradient(180deg,#1a2433,#203046 60%,#1f2f45)}
.card{top:170px;width:289px;height:348px;border:2px solid #cfd6e0;background:rgba(20,32,50,.55);color:var(--white);padding:34px 38px}
.card .q{font-family:"Lora",serif;font-size:46px;line-height:40px;font-weight:700}
.card p{font-size:13.5px;line-height:21px;color:#dce2ea;margin-top:10px}
.card .stars{color:var(--orange);font-size:15px;letter-spacing:2px;margin-top:14px}
.card .who{font-size:13px;font-weight:700;margin-top:18px}
.card .co{font-size:13.5px;color:#dce2ea}
.dot{top:556px;width:7px;height:7px;border-radius:50%;background:var(--white)}

/* process */
.process{top:3755px;height:528px;background:var(--white)}
.process-photo{left:134px;top:54px;width:543px;height:422px;background:linear-gradient(170deg,#b5c6d8 0%,#a8673c 45%,#7e5a42 75%,#5f6a4a)}
.process-title{left:730px;top:64px;font-size:38px;font-weight:700}
.step{left:740px;font-size:13.5px;line-height:18px;color:#333;padding-left:32px;width:330px}
.step::before{content:"";position:absolute;left:0;top:1px;width:18px;height:15px;background:#7a4a28;clip-path:polygon(50% 0,100% 45%,88% 45%,88% 100%,12% 100%,12% 45%,0 45%)}

/* contact / map */
.contact{top:4283px;height:337px;background:linear-gradient(120deg,#dfe7d6,#eef0ea 40%,#d6e3cf 70%,#e8ece4)}
.contact-card{left:77px;top:41px;width:328px;height:249px;background:var(--white);border-radius:8px;box-shadow:0 2px 10px rgba(0,0,0,.15);text-align:center}
.contact-card h2{font-size:25px;font-weight:700;margin-top:30px}
.contact-card h3{font-size:16px;font-weight:700;color:var(--orange);margin-top:12px;line-height:22px}
.contact-card .line{font-size:12px;color:#333;margin-top:10px;line-height:18px}

/* quote */
.quote{top:4620px;height:528px;background:linear-gradient(160deg,#3b4552 0%,#1f66b8 30%,#1b5fae 65%,#3a6c9c 100%)}
.quote-mark{left:0;width:1200px;top:165px;text-align:center;color:var(--white);font-family:"Lora",serif;font-size:60px;line-height:60px}
.quote-rule{top:196px;width:70px;height:2px;background:#cfe0f5}
.quote-text{left:0;width:1200px;top:248px;text-align:center;font-family:"Lora",serif;font-size:28px;line-height:34px;color:var(--white)}

/* footer */
.site-footer{top:5148px;height:185px;background:var(--footer)}
.footer-mark{left:190px;top:22px;width:60px;height:54px;background:#5a3a22}
.footer-name{left:132px;top:119px;font-size:20px;font-weight:900;color:var(--white)}
.footer-sub{left:132px;top:143px;font-size:14px;letter-spacing:3px;color:var(--white)}
.fsocial{top:46px;width:32px;height:32px;border-radius:50%;background:var(--white)}
.flink{top:52px;font-size:17px;color:var(--white)}
.footer-strip{left:414px;top:141px;width:786px;height:44px;background:var(--blue);clip-path:polygon(40px 0,100% 0,100% 100%,0 100%)}
.copyright{left:463px;top:155px;font-size:14px;font-weight:700;color:var(--white)}
</style>
</head>
<body>

<header class="site-header">
  <div class="abs brand-mark"></div>
  <div class="abs brand-name">GARETH WOOLSEY</div>
  <div class="abs brand-sub">Home Improvement</div>
  <div class="abs follow">FOLLOW US</div>
  <div class="abs social" style="left:784px;background:#3b5998"></div>
  <div class="abs social" style="left:818px;background:#1da1f2"></div>
  <div class="abs social" style="left:852px;background:#0e5a8a"></div>
  <svg class="abs" style="left:905px;top:22px" width="30" height="30" viewBox="0 0 30 30" fill="none" stroke="#1f5fa8" stroke-width="2">
    <path d="M11 9c2 3 2 9 0 12"/><path d="M6 5c4 5 4 15 0 20"/><path d="M19 9c-2 3-2 9 0 12"/><path d="M24 5c-4 5-4 15 0 20"/>
  </svg>
  <div class="abs call-label">CALL US NOW</div>
  <div class="abs call-number">555.204.7719</div>
  <div class="abs nav active" style="left:523px">HOME</div>
  <div class="abs nav" style="left:588px">ABOUT US</div>
  <div class="abs nav" style="left:679px">SERVICES</div>
  <div class="abs nav" style="left:768px">SERVICES</div>
  <div class="abs nav" style="left:861px">TESTIMONIALS</div>
  <div class="abs nav" style="left:987px">CONTACT US</div>
</header>

<section class="hero" role="img" aria-label="Photo of a finished redwood pergola and fenced backyard deck">
  <div class="abs hero-eyebrow">RECENT WORK</div>
  <div class="abs hero-title">HOME IMPROVEMENT<br>CONSTRUCTION</div>
  <div class="abs btn hero-btn">CONTACT US</div>
  <svg class="abs hero-arrow" style="left:38px" width="24" height="40" viewBox="0 0 24 40"><path d="M20 4 4 20l16 16" fill="none" stroke="#fff" stroke-width="4"/></svg>
  <svg class="abs hero-arrow" style="left:1140px" width="24" height="40" viewBox="0 0 24 40"><path d="M4 4l16 16L4 36" fill="none" stroke="#fff" stroke-width="4"/></svg>
</section>

<section class="welcome">
  <div class="abs portrait" role="img" aria-label="Portrait photo of Gareth Woolsey"></div>
  <div class="abs welcome-kicker">Welcome to</div>
  <div class="abs welcome-title">Gareth Woolsey</div>
  <div class="abs rule" style="left:623px;top:166px;width:50px"></div>
  <p class="abs welcome-text">Sed ut perspiciatis unde omnis iste natus error sit voluptatem accusantium doloremque laudantium, totam rem aperiam, eaque ipsa quae ab illo inventore veritatis et quasi architecto beatae vitae dicta sunt explicabo. Nemo enim ipsam voluptatem quia voluptas sit aspernatur aut odit aut fugit, sed quia consequuntur magni dolores eos qui ratione voluptatem sequi nesciunt. Neque porro quisquam est, qui dolorem ipsum quia dolor sit amet,</p>
  <div class="abs btn welcome-btn">READ MORE</div>
</section>

<section class="services">
  <h2 class="abs section-title" style="top:53px;color:#fff">Our Services</h2>
  <div class="abs title-bar" style="top:115px;background:#fff"></div>

  <div class="abs service" style="left:89px;top:195px">
    <svg width="60" height="64" viewBox="0 0 60 64" fill="none" stroke="#fff" stroke-width="2.5"><rect x="12" y="6" width="36" height="50"/><path d="M30 6v50M24 18h12M8 56h44"/><circle cx="30" cy="12" r="2"/></svg>
    Bathroom Conversions</div>
  <div class="abs service" style="left:350px;top:195px">
    <svg width="60" height="64" viewBox="0 0 60 64" fill="none" stroke="#fff" stroke-width="2.5"><path d="M8 8h40v48H8zM8 8l-4 4v48l4-4M20 20h20v20H20zM30 20v20M20 30h10"/></svg>
    Interior Design Options</div>
  <div class="abs service" style="left:607px;top:195px">
    <svg width="60" height="64" viewBox="0 0 60 64" fill="none" stroke="#fff" stroke-width="2.5"><path d="M22 14h16l-3 8H25zM30 6v8M6 30h48v24H6zM18 30v24M42 30v24M24 38h12"/></svg>
    Kitchen Remodels</div>
  <div class="abs service" style="left:859px;top:195px">
    <svg width="60" height="64" viewBox="0 0 60 64" fill="none" stroke="#fff" stroke-width="2.5"><path d="M4 30 30 10l26 20M10 26v28h40V26M24 54V38h12v16M14 34h6v6h-6zM40 34h6v6h-6z"/></svg>
    House Remodels</div>

  <div class="abs service" style="left:89px;top:370px">
    <svg width="80" height="54" viewBox="0 0 80 54" fill="none" stroke="#fff" stroke-width="3"><path d="M4 46 30 18l26 28M30 18h20l26 28M18 40h6v6h-6z"/></svg>
    Structural /<br>Architectural Options</div>
  <div class="abs service" style="left:350px;top:370px">
    <svg width="60" height="60" viewBox="0 0 60 60" fill="none" stroke="#fff" stroke-width="2.5"><path d="M6 24 30 6l24 18M10 22v32h40V22M16 44h28v8H16zM18 36h10v8H18z"/></svg>
    Room Additions</div>
  <div class="abs service" style="left:607px;top:370px">
    <svg width="60" height="60" viewBox="0 0 60 60" fill="none" stroke="#fff" stroke-width="2.5"><path d="M10 6h40v50H10zM16 12h28v38H16zM16 12l14 6v36"/></svg>
    Window Replacement</div>
  <div class="abs service" style="left:859px;top:370px">
    <svg width="60" height="60" viewBox="0 0 60 60" fill="none" stroke="#fff" stroke-width="2.5"><path d="M22 6h30v48H22zM8 24h14v30H8zM28 12h8v8h-8zM40 12h8v8h-8zM28 26h8v8h-8zM40 26h8v8h-8zM6 54h48"/></svg>
    Commercial TI</div>
</section>

<section class="projects">
  <h2 class="abs section-title" style="top:50px">Our Latest Projects</h2>
  <div class="abs title-bar" style="top:112px;background:#222"></div>

  <div class="abs tile" style="left:139px;top:168px;width:455px;height:262px;background:linear-gradient(160deg,#6f7a5a,#5a4a3c 60%,#8a7a62)" role="img" aria-label="Photo of a new shed roof and siding"></div>
  <div class="abs tile" style="left:598px;top:168px;width:453px;height:262px;background:linear-gradient(170deg,#7e8a6a,#9a4f3c 50%,#8a5a3e)" role="img" aria-label="Photo of a stained redwood deck platform"></div>

  <div class="abs tile" style="left:139px;top:435px;width:306px;height:281px;background:linear-gradient(150deg,#6d4a3a,#b0704a 55%,#8a6a4a)" role="img" aria-label="Photo of fresh redwood deck boards"></div>
  <div class="abs tile tile-feature" style="left:449px;top:435px;width:294px;height:281px">
    <h3>Gareth Woolsey<br>Home Improvement</h3>
    <div class="btn">VIEW OUR PORTFOLIO</div>
  </div>
  <div class="abs tile" style="left:747px;top:435px;width:304px;height:281px;background:linear-gradient(160deg,#a9a49a,#b07a4a 55%,#7a5a40)" role="img" aria-label="Photo of wooden deck framing and steps"></div>

  <div class="abs tile" style="left:139px;top:720px;width:455px;height:265px;background:linear-gradient(170deg,#7fa1d0,#9a8066 45%,#6a7a4a)" role="img" aria-label="Photo of a deck built beside a trailer home"></div>
  <div class="abs tile" style="left:598px;top:720px;width:453px;height:265px;background:linear-gradient(160deg,#4a5a3a,#6a5a4c 50%,#3f8aa8)" role="img" aria-label="Photo of a poolside deck with railing"></div>

  <div class="abs tile" style="left:139px;top:989px;width:306px;height:281px;background:linear-gradient(170deg,#6a4a36,#9a6a44 60%,#4a6a9a)" role="img" aria-label="Photo of a redwood pergola over a patio"></div>
  <div class="abs tile" style="left:449px;top:989px;width:294px;height:281px;background:linear-gradient(150deg,#8c8a86,#a6a39e 50%,#7e7c78)" role="img" aria-label="Photo of a cobblestone-pattern concrete walkway"></div>
  <div class="abs tile" style="left:747px;top:989px;width:304px;height:281px;background:linear-gradient(160deg,#5a3e34,#7a6a5a 50%,#8a7a62)" role="img" aria-label="Photo of stone garden steps and landscaping"></div>
</section>

<section class="testimonials">
  <h2 class="abs section-title" style="top:56px;color:#fff">Testimonials</h2>
  <div class="abs title-bar" style="top:117px;background:#fff"></div>

  <div class="abs card" style="left:143px">
    <div class="q">&ldquo;</div>
    <p>Lorem ipsum dolor sit amet, consectetur adipiscing elit, sed do eiusmod tempor incididunt ut labore et dolore magna aliqua. Ut enim ad minim veniam, quis nostrud exercitation ullamco laboris nisi ut aliquip ex ea</p>
    <div class="stars">★★★★★</div>
    <div class="who">- MRS HARLOW</div>
    <div class="co">Gareth Woolsey</div>
  </div>
  <div class="abs card" style="left:455px">
    <div class="q">&ldquo;</div>
    <p>Lorem ipsum dolor sit amet, consectetur adipiscing elit, sed do eiusmod tempor incididunt ut labore et dolore magna aliqua. Ut enim ad minim veniam, quis nostrud exercitation ullamco laboris nisi ut aliquip ex ea</p>
    <div class="stars">★★★★★</div>
    <div class="who">- ROSALIND T.</div>
    <div class="co">Gareth Woolsey</div>
  </div>
  <div class="abs card" style="left:766px">
    <div class="q">&ldquo;</div>
    <p>Lorem ipsum dolor sit amet, consectetur adipiscing elit, sed do eiusmod tempor incididunt ut labore et dolore magna aliqua. Ut enim ad minim veniam, quis nostrud exercitation ullamco laboris nisi ut aliquip ex ea</p>
    <div class="stars">★★★★★</div>
    <div class="who">- ELENA MARSH</div>
    <div class="co">Gareth Woolsey</div>
  </div>

  <div class="abs dot" style="left:538px"></div>
  <div class="abs dot" style="left:556px"></div>
  <div class="abs dot" style="left:572px;top:553px;width:13px;height:13px;background:var(--orange);border:2px solid #fff"></div>
  <div class="abs dot" style="left:594px"></div>
  <div class="abs dot" style="left:612px"></div>
</section>

<section class="process">
  <div class="abs process-photo" role="img" aria-label="Photo of a redwood pergola attached to a stucco wall"></div>
  <h2 class="abs process-title">Our Process</h2>
  <div class="abs step" style="top:160px">Lorem Ipsum is simply dummy text<br>of the printing and typesetting industry</div>
  <div class="abs step" style="top:221px">Contrary to popular belief, Lorem Ipsum</div>
  <div class="abs step" style="top:269px">There are many variations of<br>passages of Lorem Ipsum</div>
  <div class="abs step" style="top:330px">Lorem ipsum dolor sit amet, consectetur</div>
  <div class="abs step" style="top:376px">On the other hand we denounce with<br>righteous indignation</div>
  <div class="abs step" style="top:440px">Contrary to popular belief, Lorem Ipsum</div>
</section>

<section class="contact" role="img" aria-label="Street map showing the company location">
  <div class="abs contact-card">
    <h2>CONTACT INFO</h2>
    <h3>GARETH WOOLSEY HOME<br>IMPROVEMENT</h3>
    <div class="line">41 Cedar Row, Suite 2<br>Carson City, USA</div>
    <div class="line">
      <svg width="11" height="11" viewBox="0 0 24 24" style="vertical-align:-1px"><path fill="#222" d="M6.6 10.8a15 15 0 0 0 6.6 6.6l2.2-2.2a1 1 0 0 1 1-.25 11.4 11.4 0 0 0 3.6.6 1 1 0 0 1 1 1V20a1 1 0 0 1-1 1A17 17 0 0 1 3 4a1 1 0 0 1 1-1h3.5a1 1 0 0 1 1 1c0 1.25.2 2.45.6 3.6a1 1 0 0 1-.25 1z"/></svg>
      &nbsp;1-800-555-0148</div>
    <div class="line" style="margin-top:4px">
      <svg width="12" height="10" viewBox="0 0 24 18" style="vertical-align:-1px"><path fill="#222" d="M0 0h24v18H0z"/><path d="M1 1l11 9 11-9" fill="none" stroke="#fff" stroke-width="2"/></svg>
      &nbsp;info@woolseyhome.com</div>
  </div>
</section>

<section class="quote" role="img" aria-label="Aerial photo of a backyard pool surrounded by decking">
  <div class="abs quote-mark">&ldquo;</div>
  <div class="abs quote-rule" style="left:485px"></div>
  <div class="abs quote-rule" style="left:645px"></div>
  <div class="abs quote-text">Our form of relaxing is<br>taking on new projects for the<br>house. It's not work for us -<br>It's a true labor of love</div>
</section>

<footer class="site-footer">
  <div class="abs footer-mark"></div>
  <div class="abs footer-name">GARETH WOOLSEY</div>
  <div class="abs footer-sub">Home Improvement</div>
  <div class="abs fsocial" style="left:409px"></div>
  <div class="abs fsocial" style="left:459px"></div>
  <div class="abs flink" style="left:547px">About</div>
  <div class="abs flink" style="left:637px">Portfolio</div>
  <div class="abs flink" style="left:748px">Our Service</div>
  <div class="abs flink" style="left:885px">Reviews</div>
  <div class="abs flink" style="left:992px">Contact</div>
  <div class="abs footer-strip"></div>
  <div class="abs copyright">Gareth Woolsey Home Improvement © 2020.All Rights Reserved | Privacy Policy</div>
</footer>

</body>
</html>
```